New solo practice law firm is looking for an elegant, professional, and interactive web design

I need a web design and developer for a new small law firm in Sacramento, California called Dorian Kessel Law, A Professional Corporation. I am a trial lawyer who represents average people facing difficult litigation disputes, including criminal defense as a former prosecutor and civil litigation as a civil litigator. Criminal defense includes domestic violence, battery, assault, drug possession, theft, DUI, etc. Civil litigation includes business disputes, property disputes, employment disputes, family law disputes, and immigration issues. I would like to see web designs that incorporate my logo and use the logo's navy blue and gold colors. I have uploaded the files of my logo to this brief. Please only use the navy blue and gold version. Overall, I want the design to look firm, professional, and elegant.

I plan on having the following pages on my website: (1) Home, (2) Dorian Kessel, (3) Practice Areas, (4) Insights, (5) Contact. I've hand drawn a preliminary sketch concept of what I envision the home page's layout to look like (attached with a text version). I would like your design to keep a similar layout for the homepage and incorporate my logo's colors within it but I am open to creative layout alternatives/ideas. I would like the other pages to have a similar look and feel as the home page. Some of the areas currently in my sketch do not have the full text. You can insert other text for now and I will provide the winner the full text.

In terms of the pictures on the website, I enjoy images of courthouses, columns (example attached but I cannot use this one), and, if possible, images from Sacramento, CA in my background (headshot attached). A plus would be live images that move and also sections of the webpage moving in the viewers view as they scroll down on the page. Also, it would be great to have my logo act as the tab for the website. I can provide other versions of the logo if needed.

I look forward to seeing your Wordpress designs!

People needing legal representation.

Law

Coded - Design and coding required

5+ page

Serif

• Incorporate my logo and my logo's colors.
• Live pictures and images appearing as viewers scroll on page.

```html
<!DOCTYPE html>
<html lang="en">
<head>
<meta charset="utf-8">
<title>Dorian Kessel Law — A Professional Corporation</title>
<link rel="stylesheet" href="https://fonts.googleapis.com/css2?family=Montserrat:wght@400;500;600;700;800&display=swap">
<style>
:root{
  --navy:#14213d;
  --navy-deep:#0f1a31;
  --gold:#b9a070;
  --gold-light:#c9ae7c;
  --gold-dark:#a88c5c;
  --sand:#ad9265;
  --white:#ffffff;
  --ink:#1a2540;
}
*{box-sizing:border-box;margin:0;padding:0}
html,body{width:1200px;height:2918px;overflow:hidden}
body{font-family:"Montserrat",sans-serif;color:var(--ink);background:var(--white);position:relative}
.abs{position:absolute}

/* header */
.site-header{position:absolute;left:0;top:0;width:1200px;height:115px;background:var(--navy)}
.brand{position:absolute;display:flex;align-items:center;gap:14px}
.brand-mark{width:78px;height:78px;border:2px solid var(--gold)}
.brand-name{color:var(--gold);font-weight:500;text-transform:uppercase}
.brand-name .line1{display:block;font-size:21px;letter-spacing:3px}
.brand-name .line2{display:block;font-size:10px;letter-spacing:3px;margin-top:6px;text-align:center}
.header-address{left:636px;top:20px;color:var(--white);font-size:15px;line-height:24px}
.header-cta{left:902px;top:17px;color:var(--white);font-size:15px}
.header-cta .phone{color:var(--gold-light);font-weight:700;font-size:20px;margin-top:2px}
.lang-select{left:905px;top:70px;width:120px;height:28px;border:1px solid #c7cbd6;color:var(--white);font-size:11px;padding:6px 13px;display:flex;justify-content:space-between;align-items:center}

/* nav */
.main-nav{position:absolute;left:0;top:115px;width:1200px;height:56px;background:linear-gradient(90deg,var(--gold-dark),var(--gold-light) 60%,#c4a979)}
.main-nav a{position:absolute;top:20px;color:var(--white);font-weight:700;font-size:15px;letter-spacing:.5px;text-decoration:none}
.main-nav .active-bar{position:absolute;left:107px;top:52px;width:113px;height:4px;background:#e1d2b3}

/* hero */
.hero{position:absolute;left:0;top:171px;width:1200px;height:580px;background:linear-gradient(180deg,#2f7fc6 0%,#7ab2de 30%,#d9e7f1 52%,#7e8b86 64%,#3f6d49 76%,#2d5f86 88%,#b7a27a 100%)}
.hero-text{position:absolute;left:0;top:80px;width:1200px;text-align:center;color:var(--navy)}
.hero-text .welcome{font-size:25px;letter-spacing:6px;font-weight:400}
.hero-text h1{font-size:45px;font-weight:800;letter-spacing:2px;margin-top:6px}
.hero-text .rule{width:442px;height:2px;background:var(--navy);margin:6px auto 0;opacity:.7}
.hero-text .sub{font-size:21px;letter-spacing:4px;margin-top:12px}

/* intro */
.intro-title{left:112px;top:843px;font-size:30px;color:var(--navy);letter-spacing:1px}
.intro-title b{font-weight:800}
.intro-title span{font-weight:400}
.intro-rule{left:788px;top:858px;width:412px;height:2px;background:var(--gold)}
.intro-copy{left:112px;top:897px;width:980px;font-size:17.5px;line-height:31px;color:var(--ink)}
.practice-card{position:absolute;top:1011px;width:232px;height:213px;overflow:hidden}
.practice-card .photo{position:absolute;inset:0}
.practice-card .label{position:absolute;left:0;bottom:0;width:100%;height:46px;background:rgba(185,160,112,.88);color:var(--white);font-weight:700;font-size:16px;letter-spacing:.5px;padding:14px 0 0 22px}

/* about */
.about{position:absolute;left:0;top:1320px;width:1200px;height:578px;background:linear-gradient(100deg,#1d3157 0%,#162848 45%,#13213e 100%)}
.about-photo{position:absolute;left:680px;top:0;width:345px;height:578px;background:linear-gradient(180deg,#2a2a33 0%,#1b1b22 40%,#121218 100%)}
.about h2{position:absolute;left:126px;top:108px;color:var(--white);font-size:32px;font-weight:800;line-height:37px;letter-spacing:1px}
.about .rule{position:absolute;left:128px;top:192px;width:70px;height:3px;background:var(--gold)}
.about-copy{position:absolute;left:126px;top:215px;width:505px;color:var(--white);font-size:14px;line-height:24px}
.about-copy p+p{margin-top:16px}
.btn-outline{position:absolute;left:130px;top:404px;width:188px;height:43px;border:2px solid var(--gold);color:var(--white);font-weight:700;font-size:14px;display:flex;align-items:center;justify-content:center;gap:6px}

/* consult */
.consult{position:absolute;left:0;top:1898px;width:1200px;height:610px;background:linear-gradient(180deg,var(--sand) 0%,var(--sand) 55%,#b49a6c 75%,#a98e60 100%)}
.consult-corner{position:absolute;left:104px;top:56px;width:58px;height:58px;border-left:3px solid #cdb88f;border-top:3px solid #cdb88f}
.consult-form{position:absolute;left:119px;top:72px;width:458px;height:444px;background:var(--navy)}
.consult-form h3{position:absolute;left:45px;top:34px;color:var(--white);font-size:19px;font-weight:800;letter-spacing:.5px;line-height:24px}
.consult-form h3 span{color:var(--gold)}
.consult-form .rule{position:absolute;left:45px;top:66px;width:74px;height:3px;background:var(--gold)}
.field{position:absolute;left:43px;width:376px;border:1px solid #d5d8de;color:var(--white);font-size:12.5px;padding:13px 16px}
.btn-submit{position:absolute;left:46px;top:372px;width:134px;height:36px;background:var(--gold);color:var(--white);font-weight:800;font-size:15px;display:flex;align-items:center;justify-content:center}
.consult-info{position:absolute;left:643px;top:134px;width:460px}
.consult-info h2{color:var(--white);font-size:25px;font-weight:800;line-height:28px;letter-spacing:.5px}
.consult-info .rule{width:76px;height:3px;background:var(--white);margin-top:14px}
.consult-info p{color:var(--white);font-size:16px;line-height:26px;margin-top:22px}

/* footer */
.site-footer{position:absolute;left:0;top:2508px;width:1200px;height:410px;background:var(--navy);color:var(--white)}
.footer-heading{position:absolute;color:var(--gold);font-weight:800;font-size:16.5px;letter-spacing:.5px}
.footer-address{position:absolute;left:604px;top:106px;font-size:14px;line-height:23.5px}
.socials{position:absolute;left:602px;top:186px;display:flex;gap:9px}
.socials span{width:30px;height:30px;border-radius:50%;background:var(--gold-light)}
.quick-links{position:absolute;left:879px;top:94px;list-style:none;font-size:14px;line-height:23.5px}
.footer-divider{position:absolute;left:0;top:280px;width:1200px;height:1px;background:#2a375a}
.disclaimer{position:absolute;left:122px;top:306px;width:960px;font-size:13.5px;line-height:17px;color:#c6cad6}
.copyright{position:absolute;left:122px;top:360px;font-size:13px;color:#c6cad6}
</style>
</head>
<body>

<header class="site-header">
  <div class="brand" style="left:108px;top:18px">
    <div class="brand-mark"></div>
    <div class="brand-name"><span class="line1">Dorian Kessel Law</span><span class="line2">A Professional Corporation</span></div>
  </div>
  <div class="abs header-address">2210 HARBOR POINT BLVD<br>SUITE #410<br>LARKMONT, CA 95999</div>
  <div class="abs header-cta">FREE CONSULTATION<div class="phone">(916) 555-0142</div></div>
  <div class="abs lang-select">ENGLISH
    <svg width="12" height="8" viewBox="0 0 12 8"><path d="M1 1l5 5 5-5" fill="none" stroke="#fff" stroke-width="1.6"/></svg>
  </div>
</header>

<nav class="main-nav">
  <a style="left:133px">HOME</a>
  <a style="left:272px">DORIAN KESSEL</a>
  <a style="left:526px">PRACTICE AREAS</a>
  <a style="left:771px">INSIGHTS</a>
  <a style="left:940px">CONTACT</a>
  <div class="active-bar"></div>
</nav>

<section class="hero" role="img" aria-label="City skyline with a golden lift bridge and river under a blue sky">
  <div class="hero-text">
    <div class="welcome">WELCOME TO</div>
    <h1>DORIAN KESSEL LAW</h1>
    <div class="rule"></div>
    <div class="sub">A PROFESSIONAL CORPORATION</div>
  </div>
</section>

<h2 class="abs intro-title"><b>CRIMINAL AND CIVIL</b> <span>TRIAL LAWYERS</span></h2>
<div class="abs intro-rule"></div>
<p class="abs intro-copy">Dorian Kessel Law is a law firm serving the Sacramento, Yolo, San Joaquin, Solano and Stanislaus Counties. We represent clients in a wide array of criminal, family law, and immigration cases</p>

<div class="practice-card" style="left:116px">
  <div class="photo" role="img" aria-label="Handcuffed hands" style="background:linear-gradient(160deg,#3a3432,#6b5448 50%,#2a2523)"></div>
  <div class="label">CRIMINAL DEFENSE</div>
</div>
<div class="practice-card" style="left:361px">
  <div class="photo" role="img" aria-label="Lawyer in a suit signing documents" style="background:linear-gradient(160deg,#1e1f24,#3a3b40 55%,#d9d7d2)"></div>
  <div class="label">CIVIL LITIGATION</div>
</div>
<div class="practice-card" style="left:608px">
  <div class="photo" role="img" aria-label="Open road toward mountains under a cloudy sky" style="background:linear-gradient(180deg,#7f8b9a,#c0c4c6 35%,#8b7766 55%,#4a4a4e)"></div>
  <div class="label">IMMIGRATION</div>
</div>
<div class="practice-card" style="left:853px">
  <div class="photo" role="img" aria-label="Family with a smiling baby outdoors" style="background:linear-gradient(160deg,#f1ece2,#d8c3a2 45%,#7f9b5a)"></div>
  <div class="label">FAMILY LAW</div>
</div>

<section class="about">
  <div class="about-photo" role="img" aria-label="Portrait of attorney Dorian Kessel in a dark suit"></div>
  <h2>READY, RELIABLE,<br>AND EXPERIENCED</h2>
  <div class="rule"></div>
  <div class="about-copy">
    <p>Lorem ipsum dolor sit amet, consectetur adipiscing elit, sed do<br>eiusmod tempor incididunt ut labore et dolore magna aliqua.</p>
    <p>Lorem ipsum dolor sit amet, consectetur adipiscing elit, sed do<br>eiusmod tempor incididunt ut labore et dolore magna aliqua. Ut<br>enim ad minim veniam, quis nostrud exercitation ullamco laboris<br>nisi ut aliquip ex ea commodo consequat.</p>
  </div>
  <div class="btn-outline">ABOUT DORIAN
    <svg width="8" height="13" viewBox="0 0 8 13"><path d="M1 1l5.5 5.5L1 12" fill="none" stroke="#fff" stroke-width="1.6"/></svg>
  </div>
</section>

<section class="consult" role="img" aria-label="Faint gold-toned cityscape backdrop">
  <div class="consult-corner"></div>
  <div class="consult-form">
    <h3>SCHEDULE A <span>FREE CONSULATION</span></h3>
    <div class="rule"></div>
    <div class="field" style="top:90px;height:44px">Name</div>
    <div class="field" style="top:143px;height:44px">Email</div>
    <div class="field" style="top:196px;height:44px">Phone Number</div>
    <div class="field" style="top:250px;height:114px">Please enter a brief description of your case</div>
    <div class="btn-submit">SUBMIT</div>
  </div>
  <div class="consult-info">
    <h2>WHEN YOU CONTACT<br>DORIAN KESSEL LAW FOR<br>A FREE CONSULTATION</h2>
    <div class="rule"></div>
    <p>Lorem ipsum dolor sit amet, consectetur adipiscing elit, sed do eiusmod tempor incididunt ut labore.</p>
    <p style="margin-top:18px">Lorem ipsum dolor sit amet, consectetur adipiscing elit, sed do eiusmod tempor incididunt ut labore et dolore magna aliqua. Ut enim ad minim veniam, quis nostrud exercitation.</p>
  </div>
</section>

<footer class="site-footer">
  <div class="brand" style="left:123px;top:60px">
    <div class="brand-mark"></div>
    <div class="brand-name"><span class="line1">Dorian Kessel Law</span><span class="line2">A Professional Corporation</span></div>
  </div>
  <div class="footer-heading" style="left:599px;top:64px">CONTACT US</div>
  <div class="footer-address">2210 HARBOR POINT BLVD.<br>SUITE #410<br>LARKMONT, CA 95999</div>
  <div class="socials"><span></span><span></span><span></span></div>
  <div class="footer-heading" style="left:879px;top:62px">QUICK LINKS</div>
  <ul class="quick-links">
    <li>HOME</li><li>DORIAN KESSEL</li><li>PRACTICE AREAS</li><li>INSIGHTS</li><li>CONTACT</li><li>PRIVACY POLICY</li>
  </ul>
  <div class="footer-divider"></div>
  <p class="disclaimer">The information on this website is for general information purposes only. Nothing on this site should be taken as legal advice for any individual case or situation. This information is not intended to create, and receipt of viewing does not constitute an attorney-client relationship.</p>
  <p class="copyright">© Copyright 2021 All Rights Reserved</p>
</footer>

</body>
</html>
```